Church needs a graphic design/flyer layout for upcoming series

I need a multi-purpose design for promoting both our upcoming series of messages and our fall kick-off event where we will launch the messages.

Our promotion will be printed on a two-sided. One side is simple and focuses on the series and the other side has details in regards to the event. I have provided an attachment example of what we did last time.

The design needs to be multi-purpose because it will be used for our sermon Power Points, placed on our website banner, social media, etc.

• Sermon series is called “Harbor Lanterns”
• The subtitle will be “What’s keeping you from God?”
• Our name logo should be on the graphic as well.
• The subject manner will revolve around common hurdles that people face about God and Christianity: The existence of God, the exclusivity of religion, Hell, the reliability of the Bible, Hypocrisy in the church, etc.
• Our mission is “Connecting Young Families to Christ” so our focus is to reach out to families while not being exclusive to others.
• Our target audience is families with school-aged kids.
• This series is an invitational focus so we want it to be appealing to non-church goers.
• It should be attention grabbing while not being too ‘edgy’

• The front of the card will most likely consist the Sermon Series Graphic, title & subtitle of the series, and perhaps our name logo somewhere on it.
• The back of the card will invite and give the basic information for the event so that the people will be encouraged to save the date and come to the event.
• Here are some things that could be included on that advertisement:
o The name of the event: “Westbrook Commons Open Day”
o The date and time of the event: Sept 23rd @ 10:30
o Features of the event:
 Free lunch
 Children’s program
 Bouncy Castle
 Start of the “Harbor Lanterns” messages.
 Sample of topics
o Information about the church: our website and address, etc
o Engaging pictures and graphics.
• The rest of the tone and manner are the same as the sermon series graphic.
The flyer will be 11X14, like a postcard size.

Target Market(s)

Young families who are spiritually curious but not committed church attenders.

Colors

Designer to choose colors to be used in the design.

Requirements
Nice to have
• A modern and professional looking design.
Should not have
• Anything offensive or not family friendly.

```html
<!DOCTYPE html>
<html lang="en">
<head>
<meta charset="utf-8">
<title>Harbor Lanterns – Flyer</title>
<link rel="stylesheet" href="https://fonts.googleapis.com/css2?family=Lato:wght@400;700;900&display=swap">
<style>
  :root {
    --stage-light: #e9eaeb;
    --stage-dark: #2a2a2c;
    --card-bg: #e7e8e9;
    --orange: #f7941d;
    --blue: #0a78bd;
    --plum: #561a4f;
    --violet: #86298c;
    --white: #ffffff;
  }
  * { margin: 0; padding: 0; box-sizing: border-box; }
  html, body { width: 1200px; height: 509px; overflow: hidden; }
  body {
    font-family: "Lato", Arial, sans-serif;
    background: linear-gradient(to bottom, var(--stage-light) 0 318px, var(--stage-dark) 318px 100%);
    position: relative;
  }
  .card {
    position: absolute;
    top: 50px;
    width: 523px;
    height: 410px;
    background: var(--card-bg);
    overflow: hidden;
    box-shadow: 0 1px 4px rgba(0,0,0,.25);
  }
  .card--front { left: 64px; }
  .card--back { left: 613px; }
  .card__waves { position: absolute; inset: 0; width: 100%; height: 100%; }

  /* front */
  .series-title {
    position: absolute; left: 0; right: 0; top: 128px;
    text-align: center; color: var(--plum);
    font-weight: 900; font-size: 47px; letter-spacing: .5px; line-height: 1;
  }
  .series-subtitle {
    position: absolute; left: 0; right: 0; top: 186px;
    text-align: center; color: var(--plum);
    font-weight: 700; font-size: 20px;
  }
  .series-photo {
    position: absolute; left: 50px; right: 70px; top: 250px; bottom: 0;
    background: linear-gradient(to bottom, rgba(231,232,233,0) 0%, #e2c2a6 45%, #d4a582 100%);
    border-radius: 40px 40px 0 0;
  }

  /* back */
  .event-title {
    position: absolute; left: 0; right: 0; top: 120px;
    text-align: center; color: var(--plum);
    font-weight: 700; font-size: 33px; line-height: 1;
  }
  .event-date {
    position: absolute; left: 0; right: 0; top: 160px;
    text-align: center; color: var(--plum);
    font-weight: 700; font-size: 19px;
  }
  .features {
    position: absolute; left: 28px; top: 192px;
    color: var(--violet);
  }
  .features__heading { font-weight: 700; font-size: 18px; margin-bottom: 10px; }
  .features__list { list-style: none; }
  .features__list li {
    font-weight: 700; font-size: 13px; line-height: 17px;
    padding-left: 16px; position: relative;
  }
  .features__list li::before {
    content: ""; position: absolute; left: 2px; top: 6px;
    width: 6px; height: 6px; border-radius: 50%; background: var(--violet);
  }
  .church-name {
    position: absolute; left: 325px; top: 218px; width: 180px;
    display: flex; flex-direction: column; align-items: center; gap: 10px;
  }
  .church-name__dot {
    width: 72px; height: 72px; border-radius: 50%; background: var(--blue);
  }
  .church-name__text {
    font-size: 14px; font-weight: 400; color: var(--stage-dark); white-space: nowrap;
  }
  .contact {
    position: absolute; left: 0; right: 0; bottom: 0; height: 88px;
    background: var(--blue); color: var(--white);
    text-align: center; padding-top: 10px;
  }
  .contact__phone { font-weight: 700; font-size: 23px; line-height: 1.2; margin-bottom: 4px; }
  .contact__line { font-weight: 700; font-size: 11px; line-height: 15px; }
</style>
</head>
<body>

  <section class="card card--front">
    <svg class="card__waves" viewBox="0 0 523 410" preserveAspectRatio="none" aria-hidden="true">
      <path d="M0,0 H523 V52 C440,40 360,62 270,88 C170,118 70,128 0,158 Z" fill="var(--orange)"/>
      <path d="M290,0 H523 V34 C470,14 390,6 290,0 Z" fill="var(--white)"/>
      <path d="M300,0 H523 V26 C470,8 400,3 300,0 Z" fill="var(--blue)"/>
    </svg>
    <h1 class="series-title">HARBOR LANTERNS</h1>
    <p class="series-subtitle">What’s keeping you from God?</p>
    <div class="series-photo" role="img" aria-label="Photo of a row of raised fingers with small speech bubbles above them"></div>
  </section>

  <section class="card card--back">
    <svg class="card__waves" viewBox="0 0 523 410" preserveAspectRatio="none" aria-hidden="true">
      <path d="M0,0 H523 V150 C490,110 430,80 330,66 C220,52 100,50 0,52 Z" fill="var(--orange)"/>
      <path d="M0,0 H250 C180,6 90,14 0,26 Z" fill="var(--white)"/>
      <path d="M0,0 H235 C170,4 85,10 0,18 Z" fill="var(--blue)"/>
    </svg>
    <h2 class="event-title">Westbrook Commons Open Day</h2>
    <p class="event-date">Sept 23rd @ 10:30</p>
    <div class="features">
      <h3 class="features__heading">Features of the event:</h3>
      <ul class="features__list">
        <li>Free lunch</li>
        <li>Children’s program</li>
        <li>Bouncy Castle</li>
        <li>Start of the “Harbor Lanterns” messages.</li>
        <li>Sample of topics</li>
      </ul>
    </div>
    <div class="church-name">
      <span class="church-name__dot"></span>
      <span class="church-name__text">Alder Hill Family Church</span>
    </div>
    <footer class="contact">
      <p class="contact__phone">Ph: 905.555.0148</p>
      <p class="contact__line">Location: 118 Maple Ridge Road, Brookfield, ON A1B 2C3</p>
      <p class="contact__line">Email: hello@alderhillchurch.ca | Website: www.alderhillchurch.ca</p>
    </footer>
  </section>

</body>
</html>
```